Visitenkarte und Briefdesign
Zielgruppe
Limousinenservice (Stretchlimousinen)
Aufgabenstellung
Ich benötige eine Visitenkarte und ein Briefdesign in einer edlen Optik.
Auf folgender Seite können Informationen oder Bilder eingeholt werden
www.fahrt-glanzwerk.com
Ich mag einen Hintergrund in einer Lederoptik,( wie das Logo in Anhang, BILD x4)

```html
<!DOCTYPE html>
<html lang="de">
<head>
<meta charset="utf-8">
<title>Briefbogen Nobelfahrt</title>
<link rel="stylesheet" href="https://fonts.googleapis.com/css2?family=Tinos:wght@400;700&family=Open+Sans:wght@400;600&display=swap">
<style>
  :root {
    --paper: #ffffff;
    --ink: #111111;
    --muted: #8a8a8a;
    --contact-name: #3a3a3a;
    --leather-dark: #0b0b0b;
    --leather-mid: #2c2c2c;
    --brand-silver: #d9d9d9;
    --watermark: #f2f2f2;
    --signature-ink: #d9dcef;
  }
  * { margin: 0; padding: 0; box-sizing: border-box; }
  html, body { width: 846px; height: 1200px; overflow: hidden; background: var(--paper); }
  .letter {
    position: relative;
    width: 846px;
    height: 1200px;
    background: var(--paper);
    color: var(--ink);
    font-family: "Tinos", "Times New Roman", serif;
    overflow: hidden;
  }
  .brand-ribbon { position: absolute; left: 607px; top: 0; width: 166px; height: 152px; }
  .brand-name {
    position: absolute; left: 607px; top: 58px; width: 166px;
    text-align: center; color: var(--brand-silver);
    font-family: "Open Sans", Arial, sans-serif; font-weight: 600;
    font-size: 19px; letter-spacing: 0.5px;
  }
  .watermark-name {
    position: absolute; left: 100px; top: 1070px; width: 500px;
    text-align: center; color: var(--watermark);
    font-family: "Open Sans", Arial, sans-serif; font-weight: 600;
    font-size: 80px; line-height: 1;
  }
  .sender-line {
    position: absolute; left: 79px; top: 166px;
    font-family: "Open Sans", Arial, sans-serif; font-size: 8px; color: var(--ink);
  }
  .sender-line .star { color: var(--muted); font-size: 10px; }
  .fold-mark { position: absolute; left: 0; width: 37px; height: 2px; background: var(--ink); }
  .fold-mark.upper { top: 420px; }
  .fold-mark.lower { top: 801px; }
  .recipient {
    position: absolute; left: 110px; top: 318px;
    font-size: 17px; line-height: 20.2px; font-style: normal;
  }
  .subject {
    position: absolute; left: 110px; top: 420px;
    font-size: 17.5px; font-weight: 400; -webkit-text-stroke: 0.35px var(--ink);
  }
  .body-copy {
    position: absolute; left: 110px; top: 480px; width: 657px;
    font-size: 17.4px; line-height: 20.2px; text-align: justify; hyphens: auto;
  }
  .body-copy p + p { margin-top: 20.2px; }
  .signature { position: absolute; left: 96px; top: 902px; width: 276px; height: 42px; }
  .signer { position: absolute; left: 148px; top: 946px; font-size: 17px; }
  .contact {
    position: absolute; left: 620px; top: 1038px;
    font-family: "Open Sans", Arial, sans-serif; color: var(--muted);
  }
  .contact-name { font-size: 17px; color: var(--contact-name); letter-spacing: 0.6px; line-height: 20px; }
  .contact-role { font-size: 7.5px; letter-spacing: 0.4px; margin-bottom: 11px; }
  .contact-line { font-size: 10.5px; line-height: 18.5px; letter-spacing: 0.5px; }
</style>
</head>
<body>
<main class="letter">
  <div class="watermark-name" aria-hidden="true">Nobelfahrt</div>

  <svg class="brand-ribbon" viewBox="0 0 166 152" role="img" aria-label="Lederband in dunkler Lederoptik">
    <defs>
      <linearGradient id="leather-shade" x1="0" y1="0" x2="0" y2="1">
        <stop offset="0" stop-color="var(--leather-mid)"/>
        <stop offset="1" stop-color="var(--leather-dark)"/>
      </linearGradient>
      <filter id="leather-grain" x="0" y="0" width="100%" height="100%">
        <feTurbulence type="fractalNoise" baseFrequency="0.9" numOctaves="3" seed="4" result="noise"/>
        <feColorMatrix in="noise" type="matrix" values="0 0 0 0 0  0 0 0 0 0  0 0 0 0 0  0 0 0 0.55 0" result="grain"/>
        <feComposite in="grain" in2="SourceGraphic" operator="in" result="grainClip"/>
        <feMerge><feMergeNode in="SourceGraphic"/><feMergeNode in="grainClip"/></feMerge>
      </filter>
      <filter id="ribbon-shadow" x="-10%" y="-10%" width="120%" height="125%">
        <feDropShadow dx="0" dy="2" stdDeviation="2" flood-color="#000" flood-opacity="0.45"/>
      </filter>
    </defs>
    <g filter="url(#ribbon-shadow)">
      <polygon points="2,0 164,0 164,146 83,130 2,146" fill="url(#leather-shade)" filter="url(#leather-grain)"/>
    </g>
  </svg>
  <div class="brand-name">Nobelfahrt</div>

  <p class="sender-line">Mustername <span class="star">★</span> Musterstrasse 23 <span class="star">★</span> 12345 Musterstadt</p>

  <div class="fold-mark upper"></div>
  <div class="fold-mark lower"></div>

  <address class="recipient">
    Herr,<br>Mustermann<br>Sonstiges<br>12345 Stadt
  </address>

  <h1 class="subject">Ihre Überschrift</h1>

  <section class="body-copy" lang="de">
    <p>Lorem ipsum dolor sit amet, consetetur sadipscing elitr, sed diam nonumy eirmod tempor invidunt ut labore et dolore magna aliquyam erat, sed diam voluptua. At vero eos et accusam et justo duo dolores et ea rebum. Stet clita kasd gubergren, no sea takimata sanctus est Lorem ipsum dolor sit amet. Lorem ipsum dolor sit amet, consetetur sadipscing elitr,</p>
    <p>sed diam nonumy eirmod tempor invidunt ut labore et dolore magna aliquyam erat, sed diam voluptua. At vero eos et accusam et justo duo dolores et ea rebum. Stet clita kasd gubergren, no sea takimata sanctus est Lorem ipsum dolor sit amet.Lorem ipsum dolor sit amet, consetetur sadipscing elitr, sed diam nonumy eirmod tempor invidunt ut labore et dolore magna aliquyam erat, sed diam voluptua. At vero eos et accusam et justo duo dolores et ea rebum. Stet clita kasd gubergren,</p>
    <p>no sea takimata sanctus est Lorem ipsum dolor sit amet. Lorem ipsum dolor sit amet, consetetur sadipscing elitr, sed diam nonumy eirmod tempor invidunt ut labore et dolore magna aliquyam erat, sed diam voluptua. At vero eos et accusam et justo duo dolores et ea rebum. Stet clita kasd gubergren, no sea takimata sanctus est Lorem ipsum dolor sit amet.</p>
  </section>

  <svg class="signature" viewBox="0 0 276 42" role="img" aria-label="Handschriftliche Unterschrift Mustername">
    <rect x="0" y="0" width="276" height="42" rx="6" fill="var(--signature-ink)"/>
  </svg>
  <p class="signer">Mustername</p>

  <aside class="contact">
    <p class="contact-name">Karl Mustermann</p>
    <p class="contact-role">Mein Beruf Status</p>
    <p class="contact-line">Lindenallee 18</p>
    <p class="contact-line">60311 Talhausen</p>
    <p class="contact-line">Mobil: 01573/48210</p>
    <p class="contact-line">www.kanzlei-nobelfahrt.de</p>
  </aside>
</main>
</body>
</html>
```